Fliers and Brochures - Consumer Financing for Home Improvements

I have two word doc. brochures and two pdf fliers that I need redone. I want some language amended which I can provide and I want to see your input on new designs. I can link you to the company home page so you have a design reference to go off of.
555-281-7394 and miles@quarvetlending.example to reach me. This should be a very quick and simple process for a designer. I just want to ensure I can let you know the words we need removed and inserted. I will leave design options up to you. Please base it off our website i have provided below.

Target Market(s)

Consumers looking for pool and spa loans on one brochure and consumers looking for home improvement loans on the other.
The fliers are segmented for pool/spa and home improvements respectively but are targeted towards the contractors for internal use.

Industry/Entity Type

Consumer

Colors

Designer to choose colors to be used in the design.

Requirements
Must have
• Color that is in line with our webiste. Use www.quarvetlending.example and brightnestcredit.example as reference points.
• Keep the same info. but someone will need to contact me as we need a few bits of wording changed.

```html
<!DOCTYPE html>
<html lang="en">
<head>
<meta charset="utf-8">
<title>Quarvet Lending – Pool &amp; Spa Financing Flyer</title>
<link href="https://fonts.googleapis.com/css2?family=Libre+Baskerville:wght@400;700&family=Crimson+Text:wght@400;600;700&family=Source+Sans+3:wght@400;600&display=swap" rel="stylesheet">
<style>
  :root{
    --navy:#2b3a52;
    --navy-dark:#223047;
    --orange:#f7a73a;
    --orange-text:#e8830c;
    --grey-top:#f3f3f3;
    --grey-bottom:#e3e3e3;
    --cream:#fdf0da;
    --ink:#2a2a2a;
    --canvas:#e4e4e4;
    --white:#ffffff;
  }
  *{margin:0;padding:0;box-sizing:border-box}
  html,body{width:1200px;height:1200px;overflow:hidden}
  body{background:var(--canvas);position:relative;font-family:"Crimson Text",Georgia,serif;color:var(--ink)}
  .page{position:absolute;top:221px;width:540px;height:757px;overflow:hidden;background:var(--white);box-shadow:0 4px 14px rgba(0,0,0,.25)}
  .page--front{left:40px}
  .page--back{left:620px}
  .brand-plate{position:absolute;background:var(--white);border-radius:3px;display:flex;flex-direction:column;align-items:center;justify-content:center;font-family:"Libre Baskerville",Georgia,serif;font-weight:700;color:var(--navy);line-height:1}
  .brand-plate__main{font-size:22px}
  .brand-plate__sub{font-size:15px;margin-top:6px}

  /* front */
  .hero{position:absolute;left:0;top:0;width:540px;height:245px;display:block}
  .front-body{position:absolute;left:0;top:245px;width:540px;height:423px;background:linear-gradient(var(--grey-top),var(--grey-bottom))}
  .headline{position:absolute;left:0;width:540px;text-align:center;font-family:"Libre Baskerville",Georgia,serif;color:var(--navy)}
  .headline--caps{top:14px;font-size:16px;font-weight:700;letter-spacing:.2px}
  .headline--roles{top:36px;font-size:21px}
  .decision-bar{position:absolute;left:45px;top:68px;width:450px;height:40px;background:var(--orange);border-radius:14px 14px 0 0;display:flex;align-items:center;justify-content:center;font-family:"Libre Baskerville",Georgia,serif;font-weight:700;color:var(--navy);font-size:15px}
  .decision-bar strong{font-size:21px;margin-left:5px}
  .features{position:absolute;left:45px;top:108px;width:450px;height:122px;background:linear-gradient(90deg,#fcebd0,#fff6e7 50%,#fcebd0);border-radius:0 0 14px 14px;display:flex;padding:12px 10px 0 10px}
  .features__col{flex:1;list-style:none;font-size:10px;font-weight:700;line-height:1.3;color:var(--ink)}
  .features__col + .features__col{border-left:1px solid #e6d3b3;padding-left:30px}
  .features__col li{position:relative;padding-left:16px;margin-bottom:7px}
  .features__col li::before{content:"";position:absolute;left:3px;top:5px;width:3px;height:3px;border-radius:50%;background:var(--ink)}
  .perk{position:absolute;top:252px;width:110px;text-align:center}
  .perk svg{display:block;margin:0 auto;width:92px;height:92px}
  .perk__label{display:block;margin-top:8px;font-size:10px;font-weight:700;line-height:1.35}
  .perk--equity{left:80px}
  .perk--online{left:214px}
  .perk--states{left:349px}
  .cta{position:absolute;left:0;top:383px;width:540px;text-align:center;font-size:15px}
  .cta a{color:var(--orange-text);font-weight:700;text-decoration:none}
  .fineprint{position:absolute;left:0;top:405px;width:540px;text-align:center;font-size:6px}

  .footer{position:absolute;left:0;top:668px;width:540px;height:89px;background:var(--navy);color:var(--white)}
  .footer__name{position:absolute;left:27px;top:16px;font-family:"Libre Baskerville",Georgia,serif;font-size:12.5px;text-transform:uppercase;letter-spacing:.2px}
  .footer__contact{position:absolute;left:27px;top:37px;list-style:none;font-size:6.5px;line-height:1.55}
  .footer__contact li{display:flex;align-items:center;gap:6px}
  .footer__contact .phone{font-size:10px}
  .footer__contact svg{width:7px;height:7px;flex:none}
  .footer__address{position:absolute;left:118px;top:39px;display:flex;gap:6px;font-size:6.5px;line-height:1.5}
  .footer__address svg{width:7px;height:9px;flex:none}
  .badges{position:absolute;left:246px;top:24px;display:flex;gap:8px}
  .badge{width:63px;height:32px;background:var(--white)}

  /* back */
  .back-header{position:absolute;left:0;top:0;width:540px;height:170px;display:block}
  .back-title{position:absolute;left:45px;top:152px;font-family:"Libre Baskerville",Georgia,serif;font-size:18px;color:var(--navy);letter-spacing:-.2px}
  .faq{position:absolute;left:33px;top:192px;width:490px;list-style:none}
  .faq__item{position:relative;padding-left:12px;margin-bottom:11px}
  .faq__item--diamond::before{content:"";position:absolute;left:0;top:4px;width:5px;height:5px;background:var(--orange);transform:rotate(45deg)}
  .faq__q{font-family:"Libre Baskerville",Georgia,serif;font-weight:700;font-size:9.6px;color:var(--navy);margin-bottom:4px}
  .faq__a{font-family:"Source Sans 3",Arial,sans-serif;font-size:7px;line-height:1.35;color:var(--ink)}
  .faq__a a{color:var(--orange-text);font-weight:600;text-decoration:none}
  .faq__steps,.faq__bullets{font-family:"Source Sans 3",Arial,sans-serif;font-size:6.8px;line-height:1.3;padding-left:10px}
  .faq__steps li,.faq__bullets li{margin-bottom:2px;padding-left:2px}
  .faq__bullets{list-style:disc}
  .disclaimer-band{position:absolute;left:0;top:641px;width:540px;height:27px;background:var(--orange);padding:6px 45px 0 45px;font-family:"Source Sans 3",Arial,sans-serif;font-size:5.8px;line-height:1.3;color:#3a2a12}
</style>
</head>
<body>

<!-- FRONT SIDE -->
<section class="page page--front">
  <svg class="hero" viewBox="0 0 540 245" aria-hidden="false">
    <defs>
      <linearGradient id="poolTones" x1="0" y1="0" x2="0" y2="1">
        <stop offset="0" stop-color="#c6b49a"/>
        <stop offset=".33" stop-color="#9b7f66"/>
        <stop offset=".45" stop-color="#3a86d4"/>
        <stop offset=".8" stop-color="#1f66b8"/>
        <stop offset="1" stop-color="#8f8a84"/>
      </linearGradient>
    </defs>
    <rect width="540" height="245" fill="var(--navy)"/>
    <polygon role="img" aria-label="Photo of a backyard swimming pool with attached spa and stone patio" points="0,90 400,0 540,0 540,196 380,245 0,245" fill="url(#poolTones)"/>
    <line x1="0" y1="76" x2="338" y2="0" stroke="var(--white)" stroke-width="2.5"/>
    <line x1="410" y1="245" x2="540" y2="206" stroke="var(--white)" stroke-width="2.5"/>
  </svg>
  <div class="brand-plate" style="left:27px;top:24px;width:130px;height:84px">
    <span class="brand-plate__main">Quarvet</span>
    <span class="brand-plate__sub">Lending</span>
  </div>

  <div class="front-body">
    <p class="headline headline--caps">NO FEES OR DISCOUNTS TO THE</p>
    <p class="headline headline--roles">manufacturer/dealer/contractor</p>

    <div class="decision-bar">Instant decision on loans under <strong>$20,000*</strong></div>
    <div class="features">
      <ul class="features__col">
        <li>All loans funded upfront</li>
        <li>$2,000 to $150,000*</li>
        <li>Funds can be used for anything (fencing, decking, landscaping, outdoor kitchen, furniture)</li>
        <li>100% financing—no money down</li>
      </ul>
      <ul class="features__col">
        <li>Unsecured and secured loans</li>
        <li>Rates starting at 3.95%*</li>
        <li>No prepayment penalties</li>
        <li>Terms from 3-15 years</li>
        <li>Must be an authorized dealer/contractor</li>
      </ul>
    </div>

    <div class="perk perk--equity">
      <svg viewBox="0 0 92 92">
        <polygon points="46,1 91,46 46,91 1,46" fill="var(--navy)"/>
        <polygon points="46,9 83,46 46,83 9,46" fill="none" stroke="var(--white)" stroke-width="1.5"/>
        <path d="M30 47 L46 33 L62 47 L57 47 L57 60 L35 60 L35 47 Z" fill="var(--white)"/>
        <rect x="42" y="48" width="8" height="7" fill="var(--navy)"/>
      </svg>
      <span class="perk__label">No equity<br>required</span>
    </div>
    <div class="perk perk--online">
      <svg viewBox="0 0 92 92">
        <polygon points="46,1 91,46 46,91 1,46" fill="var(--navy)"/>
        <polygon points="46,9 83,46 46,83 9,46" fill="none" stroke="var(--white)" stroke-width="1.5"/>
        <rect x="33" y="31" width="26" height="30" fill="var(--white)"/>
        <g stroke="var(--navy)" stroke-width="2">
          <line x1="44" y1="38" x2="54" y2="38"/><line x1="44" y1="43" x2="54" y2="43"/>
          <line x1="37" y1="49" x2="54" y2="49"/><line x1="37" y1="54" x2="54" y2="54"/>
        </g>
        <path d="M36 34 L36 44 L39 41 L42 45 L43 44 L40 40 L44 40 Z" fill="var(--navy)"/>
      </svg>
      <span class="perk__label">Easy online<br>application</span>
    </div>
    <div class="perk perk--states">
      <svg viewBox="0 0 92 92">
        <polygon points="46,1 91,46 46,91 1,46" fill="var(--navy)"/>
        <polygon points="46,9 83,46 46,83 9,46" fill="none" stroke="var(--white)" stroke-width="1.5"/>
        <rect role="img" aria-label="Map of the United States" x="27" y="36" width="38" height="20" rx="4" fill="var(--white)"/>
      </svg>
      <span class="perk__label">Available in all<br>50 states*</span>
    </div>

    <p class="cta">Applications accepted online only. Visit <a href="#">www.quarvetlending.example</a> today.</p>
    <p class="fineprint">*Annual Percentage Rate (APR) refers to the cost of your credit as a yearly rate. APRs, loan amounts, and loan availability may vary by state and lender.</p>
  </div>

  <footer class="footer">
    <p class="footer__name">Quarvet Lending Services</p>
    <ul class="footer__contact">
      <li class="phone"><svg viewBox="0 0 10 10"><path d="M2 1 L4 1 L5 3.5 L3.8 4.5 Q4.8 6.2 6 6.5 L7 5.3 L9.5 6.3 L9.5 8.5 Q5 9.5 1.5 4.5 Z" fill="var(--white)"/></svg>1-800-555-0142</li>
      <li><svg viewBox="0 0 10 10"><rect x="0.5" y="2" width="9" height="6" fill="var(--white)"/><path d="M0.5 2 L5 5.5 L9.5 2" stroke="var(--navy)" fill="none"/></svg>info@quarvetlending.example</li>
      <li><svg viewBox="0 0 10 10"><circle cx="5" cy="5" r="4.3" fill="none" stroke="var(--white)"/><ellipse cx="5" cy="5" rx="1.8" ry="4.3" fill="none" stroke="var(--white)"/><line x1="0.7" y1="5" x2="9.3" y2="5" stroke="var(--white)"/></svg>www.quarvetlending.example</li>
    </ul>
    <div class="footer__address">
      <svg viewBox="0 0 10 13"><path d="M5 12.5 C1 7.5 0.5 6 0.5 4.5 A4.5 4.5 0 0 1 9.5 4.5 C9.5 6 9 7.5 5 12.5 Z" fill="var(--white)"/><circle cx="5" cy="4.5" r="1.7" fill="var(--navy)"/></svg>
      <span>200 Larkfield Court Suite<br>9 | Millbrook, MD<br>20000</span>
    </div>
    <div class="badges">
      <span class="badge"></span><span class="badge"></span><span class="badge"></span><span class="badge"></span>
    </div>
  </footer>
</section>

<!-- BACK SIDE -->
<section class="page page--back">
  <svg class="back-header" viewBox="0 0 540 170">
    <polygon points="0,0 540,0 540,74 300,42 0,148" fill="var(--navy)"/>
    <line x1="0" y1="128" x2="292" y2="26" stroke="var(--white)" stroke-width="2.5"/>
    <line x1="380" y1="48" x2="540" y2="75" stroke="var(--white)" stroke-width="2.5"/>
  </svg>
  <div class="brand-plate" style="left:278px;top:20px;width:108px;height:70px">
    <span class="brand-plate__main" style="font-size:18px">Quarvet</span>
    <span class="brand-plate__sub" style="font-size:13px;margin-top:5px">Lending</span>
  </div>

  <h1 class="back-title">POOL &amp; SPA CONSUMER FINANCING</h1>

  <ul class="faq">
    <li class="faq__item faq__item--diamond">
      <p class="faq__q">How do I sign up to become an authorized dealer so I can offer your financing?</p>
      <p class="faq__a">Go to <a href="#">www.brightnestcredit.example</a> and click on the "dealer" tab at the top of the page. Then click on the dealer application form to complete. Once the application is submitted to Quarvet, you will receive a confirmation email.</p>
    </li>
    <li class="faq__item faq__item--diamond">
      <p class="faq__q">Are there any dealer costs or discounts?</p>
      <p class="faq__a">There are NO costs to the dealer or contractor.</p>
    </li>
    <li class="faq__item faq__item--diamond">
      <p class="faq__q">Are there any dealer costs or discounts?</p>
      <ol class="faq__steps">
        <li>Applicant visits www.brightnestcredit.example to complete an application.</li>
        <li>Applicant receives an eligiblity decision.</li>
        <li>Qualified applicants receive an offer (e.g., Annual Percentage Rate (APR), term options, and monthly payment amount) based on their loan amount and application information.</li>
        <li>Qualified applicants choosing to proceed select an offer (e.g., APR and term).</li>
        <li>Qualified applicants are then asked to provide additional information to finalize their application.</li>
        <li>Upon loan funding, the money will be deposited into the applicant's bank account—usually within a few days.</li>
      </ol>
    </li>
    <li class="faq__item">
      <p class="faq__q">What are the loan amounts and terms available?</p>
      <ul class="faq__bullets">
        <li>Applicants may qualify for loans from $2,000 to $150,000 with loan terms up to 15 years.*</li>
        <li>Loan APRs start from 3.95% depending on loan amount and credit worthiness.*</li>
        <li>These loans are offered with no penalty for paying off early.</li>
      </ul>
    </li>
    <li class="faq__item faq__item--diamond">
      <p class="faq__q">Who is eligible for a loan through Quarvet?</p>
      <p class="faq__a">U.S. Citizens and/or legal residents over the age of 18.</p>
    </li>
    <li class="faq__item faq__item--diamond">
      <p class="faq__q">What is the verification process?</p>
      <p class="faq__a">Some applicants may be required to submit additional documentation or proof of income such as a W-2, 1099, or tax return in order to verify their income and eligibility.</p>
    </li>
    <li class="faq__item faq__item--diamond">
      <p class="faq__q">How soon do borrowers receive their money?</p>
      <p class="faq__a">Loan proceeds could be available within 1-2 business days.</p>
    </li>
    <li class="faq__item faq__item--diamond">
      <p class="faq__q">Are there any fees?</p>
      <p class="faq__a">Yes. Borrowers pay an "origination fee" which is a percent of the amount borrowed. The origination fee is typically between 1% and 5% of the loan amount, and is deducted from the loan proceeds before the loan is funded into a borrower's bank account. If a monthly payment is late, the borrower may be charged a late fee.</p>
    </li>
    <li class="faq__item faq__item--diamond">
      <p class="faq__q">Can a borrower pay extra on a monthly loan payment?</p>
      <p class="faq__a">If the borrower chooses, they may make additional loan payments or pay off their loan early without penalty or fee.</p>
    </li>
  </ul>

  <p class="disclaimer-band">*Annual Percentage Rate (APR) refers to the cost of your credit as a yearly rate. APRs, loan amounts, and loan availability may vary by state and lender. Loan offers are subject to loan approval, and for further details (including full disclosures) visit www.brightnestcredit.example.</p>

  <footer class="footer">
    <p class="footer__name">Quarvet Lending Services</p>
    <ul class="footer__contact">
      <li class="phone"><svg viewBox="0 0 10 10"><path d="M2 1 L4 1 L5 3.5 L3.8 4.5 Q4.8 6.2 6 6.5 L7 5.3 L9.5 6.3 L9.5 8.5 Q5 9.5 1.5 4.5 Z" fill="var(--white)"/></svg>1-800-555-0142</li>
      <li><svg viewBox="0 0 10 10"><rect x="0.5" y="2" width="9" height="6" fill="var(--white)"/><path d="M0.5 2 L5 5.5 L9.5 2" stroke="var(--navy)" fill="none"/></svg>info@quarvetlending.example</li>
      <li><svg viewBox="0 0 10 10"><circle cx="5" cy="5" r="4.3" fill="none" stroke="var(--white)"/><ellipse cx="5" cy="5" rx="1.8" ry="4.3" fill="none" stroke="var(--white)"/><line x1="0.7" y1="5" x2="9.3" y2="5" stroke="var(--white)"/></svg>www.quarvetlending.example</li>
    </ul>
    <div class="footer__address">
      <svg viewBox="0 0 10 13"><path d="M5 12.5 C1 7.5 0.5 6 0.5 4.5 A4.5 4.5 0 0 1 9.5 4.5 C9.5 6 9 7.5 5 12.5 Z" fill="var(--white)"/><circle cx="5" cy="4.5" r="1.7" fill="var(--navy)"/></svg>
      <span>200 Larkfield Court Suite<br>9 | Millbrook, MD<br>20000</span>
    </div>
    <div class="badges">
      <span class="badge"></span><span class="badge"></span><span class="badge"></span><span class="badge"></span>
    </div>
  </footer>
</section>

</body>
</html>
```